Larchfield Shopping Centre main sign re-design project

We would like to refresh the look of the main sign we have on the corner of a block of shops to make it more contemproary and vibrant.

A picture of the existing sign which reads Larchfield Shopping Centre can be found in attached PDF and at the following URL.

http://www.quentorprop.example.nz/~/media/Listings/Region%20One/Sample%20Town/Sample%20Town%20CBD/418207/Images/418207_1.ashx?bc=Gainsboro&as=1&h=550&w=980&ma=1

Larchfield Shopping Centre is also know locally as Larchfield Plaza, but the key word is Larchfield.

The existing signage has a flower/clover pattern on it which I think was just added to create a bit of interest. The building is located in a town surrounded by farm land.

I do quite like the organic feel of plant leaves or certain flowers - preferably New Zealand native plants for instance - the Kowhai flower or leaf block, pohutukawa, or kaka beak - reference images can be found with google image search

Geometric patterns could also be an option.

Once again the imagery is only to soften the sign and add some interest.
Updates

                                        Additional images of existing signage added

Project Deadline Extended
Reason: Closing date extended to allow for fact that lead up to Christmas is a busy time of year for many people.

Target Market(s)

The target audience is premium shopper

Industry/Entity Type

Building

Requirements
Must have
• Must have the words: Larchfield Shopping Centre.
The big M is not essential, and I would rather the emphasis was on the word Larchfield.
Should not have
• Should not be brown. We want the sign to feel more contemporary, but not too hard. The current pale brown feels too soft in comparison with the look of the building.

```html
<!DOCTYPE html>
<html lang="en">
<head>
<meta charset="utf-8">
<title>Larchfield Shopping Centre – Double Sign</title>
<link rel="stylesheet" href="https://fonts.googleapis.com/css2?family=Questrial&family=Jost:wght@500&family=Arimo&display=swap">
<style>
  :root {
    --page: #ffffff;
    --frame: #000000;
    --panel-dark: #1a1a1a;
    --panel-grey: #6f756c;
    --leaf-green: #4b6a34;
    --bright-green: #0c9a44;
    --sign-white: #ffffff;
    --box-line: #e6e6e6;
    --caption: #111111;
  }
  * { margin: 0; padding: 0; box-sizing: border-box; }
  html, body { width: 1200px; height: 1130px; overflow: hidden; background: var(--page); }
  .canvas { position: relative; width: 1200px; height: 1130px; background: var(--page); }

  .sign-frame {
    position: absolute; left: 0; top: 0; width: 1200px; height: 1009px;
    background: var(--frame);
  }
  .sign-panel {
    position: absolute; top: 14px; width: 583px; height: 986px;
    overflow: hidden;
  }
  .sign-panel--left { left: 9px; }
  .sign-panel--right { left: 608px; }

  .panel-backdrop { position: absolute; inset: 0; }
  .sign-panel--left .panel-backdrop {
    background:
      linear-gradient(115deg, transparent 0 12%, rgba(75,106,52,.55) 12% 24%, transparent 24% 40%, rgba(75,106,52,.55) 40% 62%, transparent 62%),
      linear-gradient(165deg, var(--panel-dark) 0 38%, var(--panel-grey) 58%, var(--bright-green) 100%);
  }
  .sign-panel--right .panel-backdrop {
    background:
      linear-gradient(65deg, transparent 0 18%, rgba(75,106,52,.55) 18% 38%, transparent 38% 62%, rgba(75,106,52,.55) 62% 80%, transparent 80%),
      linear-gradient(195deg, var(--panel-dark) 0 38%, var(--panel-grey) 58%, var(--bright-green) 100%);
  }

  .name-box {
    position: absolute; top: 217px; width: 588px; height: 138px;
    border: 5px solid var(--sign-white);
    background: var(--panel-dark);
    display: flex; align-items: center; justify-content: center;
    overflow: hidden;
  }
  .name-box--left { left: 8px; }
  .name-box--right { left: 604px; }
  .name-box__word {
    font-family: "Questrial", "Century Gothic", sans-serif;
    font-size: 96px; line-height: 1; letter-spacing: 3px;
    color: var(--sign-white);
    text-shadow: -3px 4px 0 var(--frame);
    white-space: nowrap;
  }

  .descriptor-box {
    position: absolute; top: 586px; width: 584px; height: 175px;
    border: 3px solid var(--box-line);
    padding: 8px 14px;
    display: flex; flex-direction: column; justify-content: center;
    font-family: "Jost", "Futura", sans-serif; font-weight: 500;
    color: var(--sign-white);
  }
  .descriptor-box--left { left: 6px; align-items: flex-start; }
  .descriptor-box--right { left: 607px; align-items: flex-end; background: rgba(26,26,26,.55); }
  .descriptor-box__main { font-size: 86px; line-height: .95; }
  .descriptor-box__sub { font-size: 58px; line-height: 1; }

  .caption {
    position: absolute; left: 36px; top: 1088px;
    font-family: "Arimo", Arial, sans-serif; font-size: 36px;
    color: var(--caption); white-space: nowrap; letter-spacing: .5px;
  }
</style>
</head>
<body>
<div class="canvas">
  <div class="sign-frame">
    <div class="sign-panel sign-panel--left">
      <div class="panel-backdrop" role="img" aria-label="Diagonal bands of green clover leaves over a dark panel fading to bright green"></div>
    </div>
    <div class="sign-panel sign-panel--right">
      <div class="panel-backdrop" role="img" aria-label="Diagonal bands of green clover leaves over a dark panel fading to bright green"></div>
    </div>

    <div class="name-box name-box--left"><span class="name-box__word">Larchfield</span></div>
    <div class="name-box name-box--right"><span class="name-box__word">Larchfield</span></div>

    <div class="descriptor-box descriptor-box--left">
      <span class="descriptor-box__main">Shopping</span>
      <span class="descriptor-box__sub">Centre</span>
    </div>
    <div class="descriptor-box descriptor-box--right">
      <span class="descriptor-box__main">Shopping</span>
      <span class="descriptor-box__sub">Centre</span>
    </div>
  </div>

  <p class="caption">DOUBLE SIGN &nbsp;&nbsp;/&nbsp; BIG M CORNER VIEW</p>
</div>
</body>
</html>
```